Construction training company needs a workshop invitation template

We need an invitation template for our professional development workshops we run for construction companies.
We would like to see designs that use the colors in our Timber Falcon Logo.
A simple, clean design with a lot of white space would be preferred.
No reverse text or italics.
The template should be done in Adobe Illustrator.

Requirements
Should not have
• Reverse text or italics

```html
<!DOCTYPE html>
<html lang="en">
<head>
<meta charset="utf-8">
<title>Timber Falcon Workshop Invitation</title>
<link rel="stylesheet" href="https://fonts.googleapis.com/css2?family=Oswald:wght@500;600;700&family=Arimo:wght@400;700&family=Noto+Serif:wght@600&display=swap">
<style>
:root{
  --backdrop:#808080;
  --lime:#d5e04a;
  --green:#2a9a31;
  --green-mid:#5aa82a;
  --brown:#5a3b2b;
  --brown-pill:#8a5a3f;
  --ink:#2d2d2d;
  --white:#ffffff;
  --mist:#dfe3df;
}
*{margin:0;padding:0;box-sizing:border-box}
html,body{width:1200px;height:1000px;overflow:hidden}
body{background:var(--backdrop);position:relative;font-family:"Arimo",Arial,sans-serif;color:var(--ink)}
.sheet{position:absolute;top:145px;width:501px;height:712px;background:linear-gradient(180deg,var(--lime) 0%,var(--green) 55%,var(--white) 72%);box-shadow:0 12px 16px rgba(0,0,0,.25);overflow:hidden}
.sheet--front{left:57px}
.sheet--back{left:602px}
.sheet__panel{position:absolute;left:10px;right:13px;top:15px;height:680px;background:var(--white);z-index:0}
.sheet--back .sheet__panel{left:12px;right:14px}
.swoosh{position:absolute;left:0;width:501px;z-index:1}
.abs{position:absolute;z-index:2}
.brand{display:flex;align-items:center;gap:12px;font-family:"Arimo",sans-serif;font-weight:700;font-size:21px;letter-spacing:2px;color:var(--brown)}
.brand__mark{width:30px;height:30px;background:var(--green-mid)}
.brand--front{left:0;right:0;top:52px;justify-content:center}
.brand--back{left:222px;top:546px}
.title{left:0;right:0;top:130px;text-align:center;font-family:"Oswald",sans-serif;font-weight:700;font-size:44px;line-height:56px;color:var(--green-mid);letter-spacing:.5px}
.lead{left:0;right:0;top:193px;text-align:center;font-size:22px;line-height:29px;color:var(--ink)}
.pill{display:flex;align-items:center;justify-content:center;border-radius:30px;color:var(--white);font-family:"Oswald",sans-serif;font-weight:600}
.pill--date{left:33px;width:435px;top:327px;height:52px;background:var(--brown-pill);font-size:25px;box-shadow:0 6px 8px rgba(0,0,0,.18)}
.pill--more{left:80px;width:343px;top:663px;height:33px;background:linear-gradient(180deg,#8fcf45,var(--green));font-size:20px;font-weight:500}
.pill--call{left:43px;width:417px;top:649px;height:46px;background:linear-gradient(180deg,#8fcf45,var(--green));font-size:29px;font-weight:500}
.venue{left:0;right:0;top:430px;text-align:center;font-size:23px}
.time{left:0;right:0;top:456px;text-align:center;font-family:"Oswald",sans-serif;font-weight:600;font-size:28px;color:var(--brown)}
.divider{left:200px;width:100px;height:1px;background:var(--green-mid)}
.note{left:0;right:0;text-align:center;font-size:14px;line-height:18px}
.free{left:0;right:0;top:618px;text-align:center;font-family:"Oswald",sans-serif;font-weight:600;font-size:25px;color:var(--brown)}
.frame-line{left:13px;right:13px;top:500px;height:196px;border:2px solid var(--lime);border-top:none;z-index:1}
.intro{left:45px;top:28px;width:420px;font-weight:700;font-size:15px;line-height:19px;color:var(--brown)}
.rule{left:45px;top:77px;width:410px;height:3px;background:linear-gradient(90deg,var(--lime),var(--green))}
.topics{left:45px;top:100px;width:420px;list-style:none;display:flex;flex-direction:column;gap:4px}
.topics li{display:flex;gap:20px;font-family:"Noto Serif",serif;font-weight:600;font-size:13px;line-height:17.5px;color:var(--ink)}
.topics svg{flex:none;margin-top:2px}
.seats{left:0;right:0;top:610px;text-align:center;font-family:"Oswald",sans-serif;font-weight:600;font-size:22px;color:var(--brown)}
</style>
</head>
<body>

<section class="sheet sheet--front" aria-label="Invitation front">
  <div class="sheet__panel"></div>
  <svg class="swoosh" style="top:280px" width="501" height="260" viewBox="0 0 501 260" aria-hidden="true">
    <defs>
      <linearGradient id="waveFront" x1="0" x2="1"><stop offset="0" stop-color="#2a9a31"/><stop offset="1" stop-color="#d5e04a"/></linearGradient>
      <linearGradient id="mistFront" x1="0" y1="0" x2="0" y2="1"><stop offset="0" stop-color="#e4e7e4"/><stop offset="1" stop-color="#ffffff"/></linearGradient>
    </defs>
    <path d="M0,150 C150,70 330,35 501,45 L501,240 L0,240 Z" fill="url(#mistFront)"/>
    <path d="M0,120 C120,60 310,10 501,18 L501,45 C330,35 150,70 0,150 Z" fill="url(#waveFront)"/>
  </svg>
  <div class="abs frame-line"></div>

  <div class="abs brand brand--front"><span class="brand__mark"></span>TIMBER FALCON</div>
  <h1 class="abs title">YOU'RE INVITED!</h1>
  <p class="abs lead">Ridgeline Builders invite you to a<br>Timber Falcon Professional<br>Development Workshop</p>
  <div class="abs pill pill--date">WEDNESDAY THE 7TH OF LUNE 2021</div>
  <p class="abs venue">At [address of venue inserted here]</p>
  <p class="abs time">7:00 AM to 12 noon</p>
  <div class="abs divider" style="top:502px" role="img" aria-label="Small divider"></div>
  <p class="abs note" style="top:514px">The case study at this workshop will be the Ridgeline<br>Builders project at 14 Banksia Rd, Mt Arden</p>
  <p class="abs note" style="top:556px">Enjoy some good coffee at the start and awesome food<br>for lunch at the end — all compliments of Ridgeline Builders</p>
  <div class="abs divider" style="top:606px" role="img" aria-label="Small divider"></div>
  <p class="abs free">And there's no charge for attending!</p>
  <div class="abs pill pill--more">See reverse side for more info...</div>
</section>

<section class="sheet sheet--back" aria-label="Invitation back">
  <div class="sheet__panel"></div>
  <svg class="swoosh" style="top:462px" width="501" height="150" viewBox="0 0 501 150" aria-hidden="true">
    <defs>
      <linearGradient id="waveBack" x1="0" x2="1"><stop offset="0" stop-color="#2a9a31"/><stop offset="1" stop-color="#d5e04a"/></linearGradient>
      <linearGradient id="mistBack" x1="0" y1="0" x2="0" y2="1"><stop offset="0" stop-color="#e4e7e4"/><stop offset="1" stop-color="#ffffff"/></linearGradient>
    </defs>
    <path d="M0,125 C170,60 340,22 501,30 L501,150 L0,150 Z" fill="url(#mistBack)"/>
    <path d="M0,100 C150,40 330,6 501,8 L501,30 C340,22 170,60 0,125 Z" fill="url(#waveBack)"/>
  </svg>

  <p class="abs intro">This is a live action workshop where you participate in and learn about..</p>
  <div class="abs rule"></div>
  <ul class="abs topics">
    <li><svg width="13" height="13" viewBox="0 0 13 13"><circle cx="6.5" cy="6.5" r="5.5" fill="none" stroke="#5aa82a"/><path d="M3.5,6.5 L5.8,8.8 L10,4" fill="none" stroke="#5aa82a" stroke-width="1.5"/></svg>How to set up a smart schedule for a construction project</li>
    <li><svg width="13" height="13" viewBox="0 0 13 13"><circle cx="6.5" cy="6.5" r="5.5" fill="none" stroke="#5aa82a"/><path d="M3.5,6.5 L5.8,8.8 L10,4" fill="none" stroke="#5aa82a" stroke-width="1.5"/></svg>How to get clarity on the building work to be done, using a 3D model</li>
    <li><svg width="13" height="13" viewBox="0 0 13 13"><circle cx="6.5" cy="6.5" r="5.5" fill="none" stroke="#5aa82a"/><path d="M3.5,6.5 L5.8,8.8 L10,4" fill="none" stroke="#5aa82a" stroke-width="1.5"/></svg>Getting everybody on to the same page</li>
    <li><svg width="13" height="13" viewBox="0 0 13 13"><circle cx="6.5" cy="6.5" r="5.5" fill="none" stroke="#5aa82a"/><path d="M3.5,6.5 L5.8,8.8 L10,4" fill="none" stroke="#5aa82a" stroke-width="1.5"/></svg>Solving construction headaches before they happen</li>
    <li><svg width="13" height="13" viewBox="0 0 13 13"><circle cx="6.5" cy="6.5" r="5.5" fill="none" stroke="#5aa82a"/><path d="M3.5,6.5 L5.8,8.8 L10,4" fill="none" stroke="#5aa82a" stroke-width="1.5"/></svg>Getting the information you need to make you more efficient and effective</li>
    <li><svg width="13" height="13" viewBox="0 0 13 13"><circle cx="6.5" cy="6.5" r="5.5" fill="none" stroke="#5aa82a"/><path d="M3.5,6.5 L5.8,8.8 L10,4" fill="none" stroke="#5aa82a" stroke-width="1.5"/></svg>How to get more satisfaction out of your work</li>
    <li><svg width="13" height="13" viewBox="0 0 13 13"><circle cx="6.5" cy="6.5" r="5.5" fill="none" stroke="#5aa82a"/><path d="M3.5,6.5 L5.8,8.8 L10,4" fill="none" stroke="#5aa82a" stroke-width="1.5"/></svg>Delivering projects in less time and at lower costs</li>
    <li><svg width="13" height="13" viewBox="0 0 13 13"><circle cx="6.5" cy="6.5" r="5.5" fill="none" stroke="#5aa82a"/><path d="M3.5,6.5 L5.8,8.8 L10,4" fill="none" stroke="#5aa82a" stroke-width="1.5"/></svg>Achieving better quality work</li>
    <li><svg width="13" height="13" viewBox="0 0 13 13"><circle cx="6.5" cy="6.5" r="5.5" fill="none" stroke="#5aa82a"/><path d="M3.5,6.5 L5.8,8.8 L10,4" fill="none" stroke="#5aa82a" stroke-width="1.5"/></svg>Ensuring a high level of worksite safety</li>
    <li><svg width="13" height="13" viewBox="0 0 13 13"><circle cx="6.5" cy="6.5" r="5.5" fill="none" stroke="#5aa82a"/><path d="M3.5,6.5 L5.8,8.8 L10,4" fill="none" stroke="#5aa82a" stroke-width="1.5"/></svg>Developing stronger relationships within the workforce</li>
    <li><svg width="13" height="13" viewBox="0 0 13 13"><circle cx="6.5" cy="6.5" r="5.5" fill="none" stroke="#5aa82a"/><path d="M3.5,6.5 L5.8,8.8 L10,4" fill="none" stroke="#5aa82a" stroke-width="1.5"/></svg>How smart collaboration can improve things for everybody</li>
    <li><svg width="13" height="13" viewBox="0 0 13 13"><circle cx="6.5" cy="6.5" r="5.5" fill="none" stroke="#5aa82a"/><path d="M3.5,6.5 L5.8,8.8 L10,4" fill="none" stroke="#5aa82a" stroke-width="1.5"/></svg>Transforming workplace culture and reducing the mental health issuest in the construction industry</li>
    <li><svg width="13" height="13" viewBox="0 0 13 13"><circle cx="6.5" cy="6.5" r="5.5" fill="none" stroke="#5aa82a"/><path d="M3.5,6.5 L5.8,8.8 L10,4" fill="none" stroke="#5aa82a" stroke-width="1.5"/></svg>Reducing rework and warranty work</li>
    <li><svg width="13" height="13" viewBox="0 0 13 13"><circle cx="6.5" cy="6.5" r="5.5" fill="none" stroke="#5aa82a"/><path d="M3.5,6.5 L5.8,8.8 L10,4" fill="none" stroke="#5aa82a" stroke-width="1.5"/></svg>Creating better results, with less time, effort and cost</li>
    <li><svg width="13" height="13" viewBox="0 0 13 13"><circle cx="6.5" cy="6.5" r="5.5" fill="none" stroke="#5aa82a"/><path d="M3.5,6.5 L5.8,8.8 L10,4" fill="none" stroke="#5aa82a" stroke-width="1.5"/></svg>Boosting customer satisfaction<br>and referrals</li>
  </ul>

  <div class="abs brand brand--back"><span class="brand__mark"></span>TIMBER FALCON</div>
  <p class="abs seats">Seats are limited, so book your spot today!</p>
  <div class="abs pill pill--call">CALL MAREN ON 0400 555 123</div>
</section>

</body>
</html>
```